Veltorquin.io - Please redesign to make it look better from current design

We already have the current website, that you can access but we think it can improve from current version.
Veltorquin is a cryptocurrency hedge fund that allow you to participate in the hedge fund with cryptocurrency such as eth.
At current phase, we are doing an ICO, then we want to make sure that the website it looks professional, beautiful and trustable enough for investors after looking at our website.
Target Market(s)
Investors
Industry/Entity Type
Investment
Coding
Coded - Design and coding required
Number of Pages Required
1 page
Look and feel

```html
<!DOCTYPE html>
<html lang="en">
<head>
<meta charset="utf-8">
<title>Veltorquin – Digital Asset Management</title>
<link href="https://fonts.googleapis.com/css2?family=Roboto:wght@300;400;500&family=Open+Sans:ital,wght@0,400;0,600;0,700;1,400&display=swap" rel="stylesheet">
<style>
:root{
  --navy:#14238a;
  --navy-deep:#101d78;
  --ink:#1c2a9c;
  --text:#333;
  --muted:#666;
  --light-blue:#c9ecfb;
  --grey-band:#efefef;
  --white:#fff;
  --line:#d6d6d6;
}
*{box-sizing:border-box;margin:0;padding:0}
html,body{width:1200px;height:2980px;overflow:hidden}
body{font-family:"Open Sans",Arial,sans-serif;color:var(--text);background:var(--white);position:relative}
section,header,footer{position:absolute;left:0;width:1200px}
.abs{position:absolute}

/* header + hero */
.site-header{top:0;height:120px}
.brand{left:80px;top:30px;display:flex;align-items:center;gap:14px;font-family:"Roboto",sans-serif;font-weight:500;font-size:30px;color:var(--navy)}
.brand-dot{width:44px;height:44px;border-radius:50%;background:var(--navy)}
.main-nav{right:80px;top:52px;display:flex;gap:0}
.main-nav a{font-family:"Roboto",sans-serif;font-size:17px;color:#111;text-decoration:none;position:absolute;white-space:nowrap}
.hero{top:0;height:680px}
.hero-title{left:78px;top:248px;font-family:"Roboto",sans-serif;font-weight:300;font-size:84px;color:var(--navy);letter-spacing:1px}
.hero-sub{left:80px;top:360px;font-family:"Roboto",sans-serif;font-weight:300;font-size:38px;color:var(--navy)}
.hero-rule{left:80px;top:434px;width:62px;height:3px;background:var(--navy)}
.hero-text{left:80px;top:466px;width:530px;font-size:19px;line-height:25px;color:#555}
.hero-art{left:620px;top:120px;width:580px;height:560px;background:radial-gradient(circle at 55% 50%,#e7ebfb 0%,#f7f8fe 55%,#fff 80%)}

/* about */
.about{top:680px;height:462px;background:var(--navy)}
.about-visual{left:80px;top:60px;width:480px;height:390px;background:linear-gradient(180deg,#0d1a5e 0%,#2b57c9 55%,#c8cbd2 82%,#e9e9ea 100%);border-radius:6px}
.section-title{font-family:"Roboto",sans-serif;font-weight:300;font-size:44px;text-transform:uppercase}
.about .section-title{left:628px;top:52px;color:var(--white)}
.about-text{left:628px;top:114px;width:490px;font-size:15.5px;line-height:25px;color:var(--white)}
.btn{display:flex;align-items:center;justify-content:center;background:var(--light-blue);color:var(--navy);font-weight:700;font-size:15px;text-transform:uppercase}
.about .btn{left:626px;top:358px;width:168px;height:52px}

/* team */
.team{top:1142px;height:558px;background:var(--grey-band)}
.team .section-title{left:0;width:1200px;text-align:center;top:46px;color:#111}
.member{top:130px;width:322px;height:384px;background:var(--white);box-shadow:0 2px 6px rgba(0,0,0,.18)}
.member-head{height:120px;border-bottom:1px solid var(--line);position:relative}
.avatar{position:absolute;left:10px;top:16px;width:90px;height:90px;border-radius:50%;background:#9a7a64}
.role{position:absolute;left:110px;top:36px;font-style:italic;font-size:15px;color:#333}
.name{position:absolute;left:110px;top:58px;font-size:17px;color:var(--navy);white-space:nowrap}
.bio{padding:18px 12px 0 14px;font-size:15px;line-height:25px;color:#555}

/* process */
.process{top:1700px;height:418px;background:var(--navy)}
.process .section-title{left:80px;top:56px;color:var(--white)}
.process-sub{left:80px;top:142px;font-family:"Roboto",sans-serif;font-size:30px;color:var(--white)}
.process-text{left:80px;top:192px;width:560px;font-size:15.5px;line-height:25px;color:var(--white)}
.process-art{left:650px;top:60px;width:440px;height:330px;background:linear-gradient(160deg,#2c2f38 0%,#4a4d56 60%,#e9ecf5 100%);border-radius:6px}

/* distribution */
.distribution{top:2118px;height:512px}
.dist-title{left:0;width:1200px;text-align:center;top:60px;font-family:"Roboto",sans-serif;font-size:28px;color:var(--ink)}
.dist-label{font-size:20px;color:#222}
.dist-label small{font-size:16px}
.dist-label span{display:block;font-size:15px;color:#444}
.remainder{left:0;width:1200px;text-align:center;top:446px;font-size:17px;color:#333}

/* footer */
.site-footer{top:2630px;height:350px;background:var(--navy);color:var(--white)}
.foot-h{top:52px;font-family:"Roboto",sans-serif;font-size:20px;text-transform:uppercase}
.foot-p{font-size:15.5px;line-height:25px}
.site-footer .btn{left:80px;top:212px;width:166px;height:50px}
.foot-brand{left:356px;top:100px;display:flex;align-items:center;gap:12px;font-family:"Roboto",sans-serif;font-size:20px;letter-spacing:3px}
.email{left:644px;top:182px;width:272px;height:50px;background:var(--white);display:flex;align-items:center;padding-left:22px;font-size:14px;color:#999}
.email-go{left:862px;top:182px;width:54px;height:50px;background:var(--light-blue);display:flex;align-items:center;justify-content:center}
.badge{left:962px;top:60px;width:150px;text-align:center;font-family:"Roboto",sans-serif;font-size:22px;letter-spacing:2px}
.badge-circle{width:92px;height:92px;border-radius:50%;background:var(--white);margin:0 auto 12px}
.social{top:226px;width:42px;height:42px;border-radius:50%;background:var(--light-blue)}
.foot-rule{left:80px;top:302px;width:1040px;height:1px;background:rgba(255,255,255,.25)}
.copyright{left:0;width:1200px;top:318px;text-align:center;font-size:15px}
</style>
</head>
<body>

<section class="hero">
  <div class="abs hero-art" role="img" aria-label="Line illustration of cryptocurrency icons: coin, rocket, bar chart, wallet and payment card joined by network lines"></div>
  <h1 class="abs hero-title">veltorquin</h1>
  <p class="abs hero-sub">Digital Asset Management</p>
  <div class="abs hero-rule"></div>
  <p class="abs hero-text">Veltorquin enable companies and investors to facilities business operation in modern digital world, including asset management on hedge fund strategy model.</p>
</section>

<header class="site-header">
  <div class="abs brand"><span class="brand-dot"></span>Veltorquin</div>
  <nav class="main-nav">
    <a style="left:-476px">Home</a>
    <a style="left:-384px">About</a>
    <a style="left:-288px">Process</a>
    <a style="left:-178px">Our Team</a>
    <a style="left:-56px">Contact</a>
  </nav>
</header>

<section class="about">
  <div class="abs about-visual" role="img" aria-label="Desktop monitor showing a blue financial trading chart"></div>
  <h2 class="abs section-title">About Us</h2>
  <p class="abs about-text">Veltorquin process and manages on hedge fund strategy models which invests in a diversified portfolio of blockchain tokens. Blockchain tokens are emerging which add a monetary incentive layer to p2p protocols and facilitate equity crowdfunding that anyone in the world can participate in. This means open source software developers can monetize their networks at the protocol level and users of the network are the equity owners of the network. For this conditions, returns will go to holders of the tokens.</p>
  <a class="abs btn">Explore More</a>
</section>

<section class="team">
  <h2 class="abs section-title">Executive Team</h2>
  <article class="abs member" style="left:80px">
    <div class="member-head"><div class="avatar" role="img" aria-label="Portrait of the director"></div><span class="role">Director</span><span class="name">Karun Lertwattana</span></div>
    <p class="bio">As a hedge fund manager. Lertwattana is the Chief Executive Officer of Eastbrook Capital LLC, an investment manager of Copperline Metal Fund SP (Long-Short Equity Fund, investing in U.S. Stock Market) and Kaito Summit Fund (Managed Futures Fund, focusing in Japanese Futures Market) Both based in Tokyo.</p>
  </article>
  <article class="abs member" style="left:442px">
    <div class="member-head"><div class="avatar" style="background:#8fa08a" role="img" aria-label="Portrait of the technical advisor"></div><span class="role">Technical advisor</span><span class="name">Niran Sothorn</span></div>
    <p class="bio">Sothorn has various experienced on cryptocurrency and blockchain technology. He created what was the world's 4th most valuable cryptocurrency in February 2014. He is also the world's first person to implement stealth addresses in QN-Wallets, improving cryptocurrency anonymity.</p>
  </article>
  <article class="abs member" style="left:806px">
    <div class="member-head"><div class="avatar" style="background:#7a4a3a" role="img" aria-label="Portrait of the marketing consultant"></div><span class="role">Marketing Consultant</span><span class="name">Pichit Wongsakul</span></div>
    <p class="bio">Wongsakul embeds a decade of experience in brand building, strategic planning, and marketing communication across the global agencies, such as Marlowe Worldgroup, Orbis Partners, Hale Bennett, Sakurado. His seasoned specialty focuses on exploring a new market insight to formulate disruptive strategies</p>
  </article>
</section>

<section class="process">
  <h2 class="abs section-title">Process</h2>
  <h3 class="abs process-sub">Hedge Fund Model</h3>
  <p class="abs process-text">Veltorquin run on closed-end fund (CEF) model which offers its shares to investors and utilize the fund to speculate and invest in the innovative blockchain tokens. Veltorquin will charge an upfront annual operation fee 4% of the money raised during the ICO. After that, the fund will charge a quarterly performance of 50% on the net profit made.</p>
  <div class="abs process-art" role="img" aria-label="Cartoon presenter pointing at a laptop screen showing a market volume table"></div>
</section>

<section class="distribution">
  <h2 class="abs dist-title">Net Profit Distribution</h2>
  <svg class="abs" style="left:0;top:0" width="1200" height="512" aria-hidden="true">
    <g stroke="#dcdcdc" stroke-width="2" fill="none">
      <path d="M194 244 H440 L516 268"/>
      <path d="M1014 244 H770 L694 268"/>
      <path d="M194 406 H440 L548 374"/>
      <path d="M1014 406 H770 L660 374"/>
    </g>
    <polygon points="604,208 694,268 660,374 548,374 516,268" fill="#c9ecfb"/>
    <g fill="#14238a">
      <circle cx="604" cy="208" r="4"/><circle cx="694" cy="268" r="4"/><circle cx="660" cy="374" r="4"/><circle cx="548" cy="374" r="4"/><circle cx="516" cy="268" r="4"/>
    </g>
    <circle cx="604" cy="292" r="26" fill="#14238a"/>
  </svg>
  <div class="abs dist-label" style="left:0;width:1200px;text-align:center;top:112px">50 %<span>of net profit is distributed to investors</span></div>
  <div class="abs dist-label" style="left:216px;top:176px">0 – 5 % <small>net profit &gt; 0%</small><span>performance fee</span></div>
  <div class="abs dist-label" style="left:788px;top:176px">&gt; 15% <small>net profit</small> &gt; 15%<span>performance fee</span></div>
  <div class="abs dist-label" style="left:254px;top:344px">5 – 10% <small>net profit</small> &gt; 5%<span>performance fee</span></div>
  <div class="abs dist-label" style="left:750px;top:344px">10-15 % <small>net profit</small> &gt; 13%<span>performance fee</span></div>
  <p class="abs remainder">The remainder (50% minus performance fee, so at least 35%) is reinvested</p>
</section>

<footer class="site-footer">
  <h4 class="abs foot-h" style="left:80px">For More Info</h4>
  <p class="abs foot-p" style="left:80px;top:92px;width:240px">Lorem Ipsum is simply dummy text of the printing and typesetting industry. Lorem Ipsum has been the industry's.</p>
  <a class="abs btn">Download PDF</a>

  <h4 class="abs foot-h" style="left:358px">Contact Info</h4>
  <div class="abs foot-brand">
    <svg width="20" height="26" viewBox="0 0 20 26" aria-hidden="true"><path d="M10 0a10 10 0 0 0-10 10c0 7 10 16 10 16s10-9 10-16A10 10 0 0 0 10 0z" fill="#fff"/><circle cx="10" cy="10" r="4" fill="#14238a"/></svg>
    Veltorquin
  </div>
  <p class="abs foot-p" style="left:390px;top:140px;width:240px">Rooms 08-12, 21B/F., North Tower, Lanternview Centre, Harbour Point, 42 Lantern Road, Tsim Sha Tsui, Kowloon, Hong Kong.</p>

  <h4 class="abs foot-h" style="left:644px">Newsletter</h4>
  <p class="abs foot-p" style="left:644px;top:92px;width:270px">Subscribe to Our Newsletter to get latest News &amp; Updates About Company</p>
  <div class="abs email">Enter Your E-Mail</div>
  <div class="abs email-go"><svg width="24" height="24" viewBox="0 0 24 24" aria-hidden="true"><path d="M2 11 22 3 16 21 11 14Z M11 14 22 3" fill="none" stroke="#14238a" stroke-width="2" stroke-linejoin="round"/></svg></div>

  <div class="abs badge"><div class="badge-circle"></div>Veltorquin</div>
  <span class="abs social" style="left:964px"></span>
  <span class="abs social" style="left:1014px"></span>
  <span class="abs social" style="left:1066px"></span>

  <div class="abs foot-rule"></div>
  <p class="abs copyright">© <b>Veltorquin</b> - 2017. All Rights Reserved.</p>
</footer>

</body>
</html>
```